Wellness Coach/personal trainer Business Card Design Project

We need an eye catching logo design for a wellness coach / personal trainer who specializes in weight loss / body transformation / health coaching. We educate, empower, and support our clients on their weight loss journey. We want the look and feel described below on the business card design.

Target Market(s)

80 % women 20 % men
educated 30 - 50 women
vanity/appearance focused

Industry/Entity Type

Personal Trainer

Font styles to use
Serif

Colors
a54599
f9ed23
ffffff

Requirements
Must have
• name - Dorian Calvaske
phone - (888) 275 9146
web address - www.7PennyMover.example
tagline - Becasue Looking Good Matters
Nice to have
• see Look and Feel
Colorful, Playful, Elegant
Should not have
• no cartoons or animation

```html
<!DOCTYPE html>
<html lang="en">
<head>
<meta charset="utf-8">
<title>Dorian Calvaske — Business Card</title>
<link rel="stylesheet" href="https://fonts.googleapis.com/css2?family=Bebas+Neue&family=Raleway:wght@300;400&display=swap">
<style>
  :root {
    --purple: #a54599;
    --yellow: #f9ed23;
    --white: #ffffff;
    --backdrop: #2e2e2e;
    --display: "Bebas Neue", "Oswald", sans-serif;
    --body: "Raleway", "Helvetica Neue", sans-serif;
  }
  * { box-sizing: border-box; margin: 0; padding: 0; }
  html, body {
    width: 1200px; height: 1200px; overflow: hidden;
    background: var(--backdrop);
  }
  .sheet {
    position: relative; width: 1200px; height: 1200px;
  }
  .card {
    position: absolute; left: 180px;
    width: 840px; height: 480px;
    overflow: hidden;
  }
  .card--back { top: 90px; background: var(--purple); }
  .card--front { top: 630px; background: var(--yellow); }

  /* back side */
  .back-name {
    position: absolute; left: 64px; top: 70px;
    font-family: var(--display); font-size: 84px; line-height: 1;
    color: var(--white); letter-spacing: 1px;
  }
  .back-title {
    position: absolute; left: 66px; top: 162px;
    font-family: var(--body); font-weight: 300; font-size: 30px;
    color: var(--white);
  }
  .back-rule {
    position: absolute; left: 66px; top: 250px;
    width: 4px; height: 160px; background: var(--white);
  }
  .contact-list {
    position: absolute; left: 100px; top: 262px;
    list-style: none;
  }
  .contact-item {
    display: flex; align-items: center; gap: 20px;
    height: 64px;
    font-family: var(--body); font-weight: 300; font-size: 30px;
    color: var(--white);
  }
  .contact-icon { width: 34px; height: 34px; flex: none; }

  /* front side */
  .front-name {
    position: absolute; left: 62px; top: 78px;
    font-family: var(--display); font-size: 116px; line-height: 0.86;
    color: var(--purple); letter-spacing: 1px;
  }
  .front-title {
    position: absolute; left: 64px; top: 290px;
    font-family: var(--display); font-size: 34px; line-height: 1.02;
    color: var(--white); letter-spacing: 0.5px;
  }
  .front-rule {
    position: absolute; left: 452px; top: 70px;
    width: 5px; height: 350px; background: var(--white);
  }
  .tagline {
    position: absolute; left: 500px; top: 76px;
    font-family: var(--display); font-size: 100px; line-height: 0.86;
    color: var(--white); letter-spacing: 1px;
  }
</style>
</head>
<body>
<main class="sheet">
  <section class="card card--back" aria-label="Business card, back">
    <h2 class="back-name">Dorian Calvaske</h2>
    <p class="back-title">Wellness Coach &amp; Personal Trainer</p>
    <div class="back-rule"></div>
    <ul class="contact-list">
      <li class="contact-item">
        <svg class="contact-icon" viewBox="0 0 24 24" aria-hidden="true">
          <path fill="#f9ed23" d="M6.6 10.8a15.1 15.1 0 0 0 6.6 6.6l2.2-2.2a1 1 0 0 1 1-.25 11.4 11.4 0 0 0 3.6.57 1 1 0 0 1 1 1V20a1 1 0 0 1-1 1A17 17 0 0 1 3 4a1 1 0 0 1 1-1h3.5a1 1 0 0 1 1 1c0 1.25.2 2.45.57 3.57a1 1 0 0 1-.25 1z"/>
        </svg>
        <span>(888) 275 9146</span>
      </li>
      <li class="contact-item">
        <svg class="contact-icon" viewBox="0 0 24 24" aria-hidden="true">
          <g fill="none" stroke="#f9ed23" stroke-width="2">
            <circle cx="12" cy="12" r="9"/>
            <ellipse cx="12" cy="12" rx="4" ry="9"/>
            <path d="M3 12h18"/>
          </g>
        </svg>
        <span>www.7PennyMover.example</span>
      </li>
    </ul>
  </section>

  <section class="card card--front" aria-label="Business card, front">
    <h1 class="front-name">Dorian<br>Calvaske</h1>
    <p class="front-title">Wellness Coach<br>&amp; Personal Trainer</p>
    <div class="front-rule"></div>
    <p class="tagline">Because<br>Looking<br>Good<br>Matters</p>
  </section>
</main>
</body>
</html>
```